Brook Lanternfield Needs a new website!

We need a four page website for a new company based in San Francisco. We help companies connect better with their clients, employees, and vendors by implementing collaborative technology.
Similar Websites
Ridge Tinkers - http://www.ridgetinkers-example.com/
Mossvantage - http://www.mossvantage-example.com/ - I don't like the the rotating window or the pictures of people. I like the icons used to go to the next pages.
Color Combos
Blues and Yellows - http://www.example-palettes.com/schemes/96/Palette96.html
We prefer graphics over the actual pictures of people in the header. Pictures of people working together in the text is fine.
Web Page Layout
Index
Cloud Advisory Services
Email Everywhere
CRM Implementation
For detailed copy please see this link https://docs.example.com/a/quillmarten.com/document/d/7XkPqTrWmZsLnBvYhJdFgCaEuNoRiStUvWxYzAbCdEf/edit
Industry/Entity Type
It Company

```html
<!DOCTYPE html>
<html lang="en">
<head>
<meta charset="utf-8">
<title>Brook Lanternfield</title>
<link href="https://fonts.googleapis.com/css2?family=Source+Sans+3:wght@300;400;600;700&display=swap" rel="stylesheet">
<style>
:root{
  --blue:#2d63b8;
  --blue-deep:#1f4f9c;
  --hero-a:#3f74ad;
  --hero-b:#2b5b93;
  --yellow:#f7c51b;
  --band-yellow:#fccb08;
  --navy:#0c1c36;
  --ink:#3a3a3a;
  --muted:#8c8c8c;
  --pale:#f3f3f3;
  --white:#ffffff;
  --dark-btn:#2e2e2e;
}
*{box-sizing:border-box;margin:0;padding:0}
html,body{width:1200px;height:2410px;overflow:hidden}
body{position:relative;font-family:"Source Sans 3",sans-serif;color:var(--ink);background:var(--white)}
.abs{position:absolute}
.center{left:0;width:1200px;text-align:center}

/* header */
.site-header{top:0;left:0;width:1200px;height:125px;background:var(--white)}
.brand{left:96px;top:50px;display:flex;align-items:center;gap:12px}
.brand-mark{width:26px;height:26px;border-radius:50%;background:var(--blue)}
.brand-name{font-size:34px;font-weight:700;color:var(--blue);letter-spacing:-0.3px}
.phone{left:875px;top:20px;display:flex;align-items:center;gap:8px;font-size:26px;font-weight:700;color:var(--blue)}
.main-nav{top:80px;left:600px;display:flex;gap:22px;font-size:14px;color:var(--ink)}
.main-nav a{color:inherit;text-decoration:none;position:relative}
.main-nav .active{color:var(--blue);font-weight:600}
.nav-marker{left:604px;top:120px;width:86px;height:5px;background:var(--yellow)}

/* hero */
.hero{top:125px;left:0;width:1200px;height:502px;background:radial-gradient(ellipse at 60% 35%,#6f9cc8 0%,var(--hero-a) 40%,var(--hero-b) 100%)}
.hero-title{top:265px;font-size:52px;font-weight:600;color:var(--yellow);letter-spacing:-0.5px}
.hero-sub{top:328px;font-size:22px;line-height:29px;color:var(--white);font-weight:400}
.btn{display:flex;align-items:center;justify-content:center;font-size:26px;font-weight:400;text-transform:uppercase}
.btn-contact{left:353px;top:448px;width:241px;height:56px;background:var(--white);color:#222}
.btn-learn{left:623px;top:448px;width:241px;height:56px;background:var(--dark-btn);color:var(--white)}

/* services */
.services{top:627px;left:0;width:1200px;height:623px;background:#fbfbfb}
.section-title{font-size:39px;font-weight:400;color:var(--ink)}
.section-sub{font-size:15px;color:var(--muted);line-height:23px;font-weight:300}
.divider{height:1px;background:#dcdcdc}
.divider-notch{width:14px;height:14px;border-right:1px solid #dcdcdc;border-bottom:1px solid #dcdcdc;transform:rotate(45deg);background:inherit}
.service{width:300px;text-align:center}
.service-ring{width:176px;height:176px;border-radius:50%;background:#ececec;margin:0 auto;display:flex;align-items:center;justify-content:center}
.service-icon{width:154px;height:154px;border-radius:50%;background:var(--blue)}
.service-title{margin-top:24px;font-size:27px;color:var(--yellow);font-weight:400}
.service-text{margin:10px auto 0;width:280px;font-size:12.5px;line-height:17px;color:var(--muted)}
.col-rule{width:1px;height:316px;top:880px;background:#dedede}

/* what we do */
.what{top:1250px;left:0;width:1200px;height:473px;background:var(--pale)}
.capability{width:160px;text-align:center}
.capability-icon{width:52px;height:52px;margin:0 auto;border-radius:8px}
.capability-label{margin-top:14px;font-size:16px;color:var(--ink)}

/* partner */
.partner{top:1723px;left:0;width:1200px;height:252px;background:var(--band-yellow)}
.partner-title{top:1762px;font-size:39px;color:#1d1d1d;font-weight:400}
.partner-sub{top:1818px;font-size:17px;color:#1d1d1d}
.partner-rule{left:164px;top:1858px;width:835px;height:2px;background:#333}
.btn-signup{left:482px;top:1898px;width:199px;height:45px;background:var(--blue);color:var(--white);font-size:21px}

/* footer */
.site-footer{top:1975px;left:0;width:1200px;height:435px;background:var(--navy);color:#c9d0dc}
.footer-brand{left:80px;top:2110px;display:flex;align-items:center;gap:14px}
.footer-brand .brand-mark{width:34px;height:34px;background:var(--blue)}
.footer-brand .brand-name{font-size:40px;color:#b8c0cc}
.footer-tagline{left:128px;top:2165px;font-size:12px;letter-spacing:2px;color:#9aa3b1;text-transform:uppercase}
.footer-head{font-size:21px;color:var(--white);font-weight:400}
.footer-rule{height:2px;background:#2a4d86}
.email-field{left:482px;top:2144px;width:177px;height:36px;background:#5a6270;border:1px solid #8a919c;font-size:11px;color:#aab0ba;padding:11px 8px}
.btn-join{left:668px;top:2144px;width:61px;height:36px;background:var(--yellow);color:#222;font-size:12px;font-weight:600;display:flex;align-items:center;justify-content:center}
.join-note{left:487px;top:2195px;font-size:12px;color:#aab0ba}
.social{top:2227px;width:35px;height:35px;border:1px solid #6e7887;display:flex;align-items:center;justify-content:center}
.social span{width:11px;height:11px;background:#c9d0dc;border-radius:2px}
.contact-row{left:820px;display:flex;gap:12px;font-size:13px;line-height:22px;color:#c9d0dc;align-items:flex-start}
.contact-row svg{margin-top:4px;flex:none}
.copyright{top:2343px;font-size:13px;color:#aab0ba}
.copy-rule{left:374px;top:2370px;width:429px;height:1px;background:#3b4a63}
</style>
</head>
<body>

<header class="site-header abs">
  <div class="brand abs"><span class="brand-mark"></span><span class="brand-name">Brook Lanternfield</span></div>
  <div class="phone abs">
    <svg width="26" height="26" viewBox="0 0 26 26" aria-hidden="true"><circle cx="13" cy="13" r="11.5" fill="none" stroke="#2d63b8" stroke-width="2"/><path d="M9 7.5l2.2-.5 1.3 3-1.5 1.1a7 7 0 0 0 3.4 3.4l1.1-1.5 3 1.3-.5 2.2c-5 .6-9.6-4-9-9z" fill="#2d63b8"/></svg>
    555-014-2026-880
  </div>
  <nav class="main-nav abs">
    <a class="active" href="#">Home</a>
    <a href="#">Cloud Advisory Services</a>
    <a href="#">Email Everywhere</a>
    <a href="#">CRM Implementation</a>
  </nav>
  <div class="nav-marker abs"></div>
</header>

<section class="hero abs" role="img" aria-label="Soft blue sky with large faint cloud shapes"></section>
<h1 class="hero-title abs center">Welcome To The Brook Lanternfield</h1>
<p class="hero-sub abs center">We help companies connect better with their clients, employees, and vendors by implementing<br>collaborative technology.</p>
<a class="btn btn-contact abs">Contact Us</a>
<a class="btn btn-learn abs">Learn More</a>

<section class="services abs"></section>
<h2 class="section-title abs center" style="top:700px">OUR CLOUD SERVICES</h2>
<p class="section-sub abs center" style="top:765px">Ridge Tinkers provides unrivaled cloud advisory and technology services for the world's leading brands.</p>
<div class="divider abs" style="left:370px;top:814px;width:460px"></div>
<div class="divider-notch abs" style="left:603px;top:806px;background:#fbfbfb"></div>

<div class="service abs" style="left:91px;top:869px">
  <div class="service-ring"><div class="service-icon" role="img" aria-label="Icon of a head with a cloud of thought"></div></div>
  <h3 class="service-title">Cloud Advisory</h3>
  <p class="service-text">Forward- thinking organizations would like to be more collaborative, flexible and productive. Put your cloud program on the path to success with our Advisory Services.</p>
</div>
<div class="col-rule abs" style="left:422px"></div>
<div class="service abs" style="left:465px;top:869px">
  <div class="service-ring"><div class="service-icon" role="img" aria-label="Icon of an envelope on a cloud"></div></div>
  <h3 class="service-title">Email Everywhere</h3>
  <p class="service-text">Drive forward your business with innovative solutions for the enterprise with either Fernleaf Suite or Quillwork Office. Experience improved collaboration, security, mobility while increasing your overall IT investment.</p>
</div>
<div class="col-rule abs" style="left:803px"></div>
<div class="service abs" style="left:823px;top:869px">
  <div class="service-ring"><div class="service-icon" role="img" aria-label="Icon of a gear, cycle arrows and a contact card"></div></div>
  <h3 class="service-title">CRM Solutions</h3>
  <p class="service-text">CRMs (Customer Relationship Management) can be complex and slow for employees to adopt. Accelerate your CRM adoption by selecting the right simple solution for your business.</p>
</div>

<section class="what abs"></section>
<h2 class="section-title abs center" style="top:1328px">What We Do</h2>
<p class="section-sub abs center" style="top:1391px">We challenge the status quo by providing unique insights, emerging strategies and proven best practices.<br>Our unwavering focus is on customer satisfaction</p>
<div class="divider abs" style="left:160px;top:1479px;width:840px"></div>
<div class="divider-notch abs" style="left:573px;top:1471px;background:var(--pale)"></div>

<div class="capability abs" style="left:148px;top:1543px"><div class="capability-icon" style="background:linear-gradient(#3d6fc2,#1f4f9c)" role="img" aria-label="Light bulb icon"></div><p class="capability-label">Strategy</p></div>
<div class="capability abs" style="left:322px;top:1543px"><div class="capability-icon" style="border-radius:50%;background:radial-gradient(circle at 40% 35%,#8ec3ea,#2a6fb4)" role="img" aria-label="Globe with arrow icon"></div><p class="capability-label">Migration</p></div>
<div class="capability abs" style="left:495px;top:1543px"><div class="capability-icon" style="background:linear-gradient(#e9e9e9,#c9c9c9)" role="img" aria-label="Implementation illustration in grey and red"></div><p class="capability-label">Implementation</p></div>
<div class="capability abs" style="left:668px;top:1543px"><div class="capability-icon" style="background:linear-gradient(#9a9a9a,#4a4a4a)" role="img" aria-label="Gear and puzzle piece icon"></div><p class="capability-label">Integration</p></div>
<div class="capability abs" style="left:842px;top:1543px"><div class="capability-icon" style="background:linear-gradient(#f2f2f2,#7fc3e6)" role="img" aria-label="Presentation board illustration"></div><p class="capability-label">Management</p></div>

<section class="partner abs"></section>
<h2 class="partner-title abs center">Partner up</h2>
<p class="partner-sub abs center">Become a member of cloud and we can implement systems for your clients too.</p>
<div class="partner-rule abs"></div>
<svg class="abs" style="left:572px;top:1857px" width="22" height="12" viewBox="0 0 22 12" aria-hidden="true"><path d="M0 1h22L11 11z" fill="#fccb08"/><path d="M0 1l11 10L22 1" fill="none" stroke="#333" stroke-width="2"/></svg>
<a class="btn btn-signup abs">Sign Up</a>

<footer class="site-footer abs"></footer>
<div class="footer-brand abs"><span class="brand-mark"></span><span class="brand-name">Brook Lanternfield</span></div>
<p class="footer-tagline abs">Creativity · Technology · Collaboration</p>

<h3 class="footer-head abs" style="left:482px;top:2060px">Get Latest Updates</h3>
<div class="footer-rule abs" style="left:466px;top:2096px;width:305px"></div>
<div class="email-field abs">Email Address</div>
<div class="btn-join abs">Join</div>
<p class="join-note abs">Join Us &amp; Sign Up T</p>
<div class="social abs" style="left:483px"><span></span></div>
<div class="social abs" style="left:536px"><span></span></div>
<div class="social abs" style="left:590px"><span></span></div>
<div class="social abs" style="left:642px"><span></span></div>
<div class="social abs" style="left:692px"><span></span></div>

<h3 class="footer-head abs" style="left:834px;top:2060px">Contact Us</h3>
<div class="footer-rule abs" style="left:811px;top:2096px;width:302px"></div>
<div class="contact-row abs" style="top:2139px">
  <svg width="14" height="14" viewBox="0 0 14 14" aria-hidden="true"><path d="M2 1.5l3-.5 1.5 3.2-1.7 1.2a7.5 7.5 0 0 0 3.8 3.8l1.2-1.7 3.2 1.5-.5 3C6 13 1 8 2 1.5z" fill="#f7c51b"/></svg>
  <span>+00 12 345 6789 0</span>
</div>
<div class="contact-row abs" style="top:2175px">
  <svg width="14" height="14" viewBox="0 0 14 14" aria-hidden="true"><rect x="1" y="3" width="12" height="9" fill="#f7c51b"/><path d="M1 3l6 5 6-5" fill="none" stroke="#0c1c36" stroke-width="1.3"/></svg>
  <span>hello@brooklanternfield.example</span>
</div>
<div class="contact-row abs" style="top:2212px">
  <svg width="14" height="18" viewBox="0 0 14 18" aria-hidden="true"><path d="M7 1a6 6 0 0 1 6 6c0 4.5-6 10-6 10S1 11.5 1 7a6 6 0 0 1 6-6z" fill="#f7c51b"/><circle cx="7" cy="7" r="2.3" fill="#0c1c36"/></svg>
  <span>lantern lane 48 block<br>harbor road east side</span>
</div>

<p class="copyright abs center">© 2014 cloud All Rights Reserved.</p>
<div class="copy-rule abs"></div>

</body>
</html>
```